Financial firm simple design

Classic business card design for a financial fund. 2 sided card- white on both sides.. One with just the company name centered and the other w the info. info included on that is :

Name
Company position
phone number
fax
email
website

Industry/Entity Type

Financial

```html
<!DOCTYPE html>
<html lang="en">
<head>
<meta charset="utf-8">
<title>Norvale Capital – Business Card</title>
<link href="https://fonts.googleapis.com/css2?family=Cinzel:wght@400&family=Quicksand:wght@500;700&display=swap" rel="stylesheet">
<style>
  :root {
    --page-bg: #ecebe8;
    --card-white: #f7f7f6;
    --brand-ink: #1f2a3a;
    --name-blue: #2f5d8a;
    --body-grey: #4a4f57;
  }
  * { margin: 0; padding: 0; box-sizing: border-box; }
  html, body {
    width: 1200px;
    height: 1000px;
    overflow: hidden;
    background: var(--page-bg);
  }
  .canvas {
    position: relative;
    width: 1200px;
    height: 1000px;
  }
  .card {
    position: absolute;
    left: 290px;
    width: 620px;
    height: 354px;
    border-radius: 4px;
    background: var(--card-white);
    box-shadow: 0 10px 28px rgba(0,0,0,0.16);
  }
  .card--info { top: 110px; }
  .card--brand {
    top: 536px;
    display: flex;
    align-items: center;
    justify-content: center;
  }
  .wordmark {
    font-family: 'Cinzel', serif;
    font-weight: 400;
    letter-spacing: 0.06em;
    white-space: nowrap;
    color: var(--brand-ink);
  }
  .card--info .wordmark {
    position: absolute;
    left: 44px;
    top: 160px;
    font-size: 25px;
  }
  .card--brand .wordmark { font-size: 40px; }
  .contact {
    position: absolute;
    left: 392px;
    top: 44px;
    font-family: 'Quicksand', sans-serif;
  }
  .contact__name {
    font-weight: 700;
    font-size: 19px;
    line-height: 1.2;
    color: var(--name-blue);
    letter-spacing: 0.02em;
  }
  .contact__role {
    font-weight: 500;
    font-size: 12px;
    color: var(--body-grey);
    margin: 2px 0 0 2px;
    letter-spacing: 0.04em;
  }
  .contact__list {
    list-style: none;
    margin-top: 18px;
  }
  .contact__item {
    display: flex;
    align-items: center;
    gap: 10px;
    font-weight: 500;
    font-size: 12.5px;
    line-height: 1.2;
    color: var(--body-grey);
    margin-bottom: 14px;
    letter-spacing: 0.03em;
    white-space: nowrap;
  }
  .contact__icon {
    width: 13px;
    height: 13px;
    flex: none;
    fill: none;
    stroke: var(--name-blue);
    stroke-width: 1.6;
  }
  .contact__icon--solid { fill: var(--name-blue); stroke: none; }
</style>
</head>
<body>
<main class="canvas">
  <section class="card card--info">
    <div class="wordmark">Norvale Capital</div>
    <div class="contact">
      <div class="contact__name">Rohan Mehra</div>
      <div class="contact__role">Director</div>
      <ul class="contact__list">
        <li class="contact__item">
          <svg class="contact__icon contact__icon--solid" viewBox="0 0 24 24" aria-hidden="true"><path d="M6.6 10.8a15.1 15.1 0 0 0 6.6 6.6l2.2-2.2c.3-.3.7-.4 1-.2 1.1.4 2.3.6 3.6.6.6 0 1 .4 1 1V20c0 .6-.4 1-1 1A17 17 0 0 1 3 4c0-.6.4-1 1-1h3.5c.6 0 1 .4 1 1 0 1.3.2 2.5.6 3.6.1.3 0 .7-.2 1z"/></svg>
          <span>+91 98 10 55 2030</span>
        </li>
        <li class="contact__item">
          <svg class="contact__icon" viewBox="0 0 24 24" aria-hidden="true"><rect x="6" y="3" width="12" height="6"/><rect x="3" y="9" width="18" height="8" rx="1"/><rect x="6" y="14" width="12" height="7"/></svg>
          <span>+91 98 10 55 2031</span>
        </li>
        <li class="contact__item">
          <svg class="contact__icon" viewBox="0 0 24 24" aria-hidden="true"><rect x="3" y="5" width="18" height="14" rx="1"/><path d="M3 6l9 7 9-7"/></svg>
          <span>hello@norvalecap.com</span>
        </li>
        <li class="contact__item">
          <svg class="contact__icon" viewBox="0 0 24 24" aria-hidden="true"><circle cx="12" cy="12" r="9"/><path d="M3 12h18M12 3c3 3 3 15 0 18M12 3c-3 3-3 15 0 18"/></svg>
          <span>www.norvalecap.com</span>
        </li>
      </ul>
    </div>
  </section>

  <section class="card card--brand">
    <div class="wordmark">Norvale Capital</div>
  </section>
</main>
</body>
</html>
```